Poster Design Project

I would like to include a picture of me meditating-
Include text: What are benefits of meditation-manage stress, reduce anxiety,improve relationships,create inner peace, awaken intuition, aid sleep patterns, lower blood pressure,become less judgemental, connect to spirit
2nd section- What is meditation: a tool to discover the bodies own inner intelligence.Its not about forcing the mind to be quiet, its about finding the stillness thats already there.
3rd section:
How will meditation improve my health? Doctors are increasingly citing stress as a major contributing factor to most illnesses.Research has shown meditation to be beneficial for wide range of health problems. As stress is greatly reduced through meditation- our minds and our bodies begin to function with maximum effectiveness.
I would like colours to be relaxing and soothing.

```html
<!DOCTYPE html>
<html lang="en">
<head>
<meta charset="utf-8">
<title>Calmora – Meditation Poster</title>
<link href="https://fonts.googleapis.com/css2?family=Didact+Gothic&family=Nunito:wght@800&family=Open+Sans:wght@600&display=swap" rel="stylesheet">
<style>
  :root {
    --page-bg: #e6e6e6;
    --panel-blue: rgba(38, 104, 178, 0.62);
    --text-white: #ffffff;
    --forest-dark: #2f4a2a;
    --forest-mid: #5f8a3c;
    --leaf-light: #b7d36a;
    --sky: #cfe6f2;
    --rock: #6b5a3c;
    --water: #2d8f9a;
    --water-deep: #1d5f6e;
    --dress-white: #f4f4f2;
    --hair-gold: #c79a5e;
  }
  * { margin: 0; padding: 0; box-sizing: border-box; }
  html, body { width: 1200px; height: 900px; overflow: hidden; background: var(--page-bg); }
  .poster {
    position: absolute; left: 241px; top: 0; width: 719px; height: 900px; overflow: hidden;
  }
  .scene-photo {
    position: absolute; inset: 0;
    background:
      radial-gradient(ellipse 120px 320px at 60px 600px, rgba(220,235,240,0.55), transparent 70%),
      radial-gradient(ellipse 90px 200px at 660px 650px, rgba(220,235,240,0.45), transparent 70%),
      linear-gradient(180deg, var(--forest-dark) 0%, var(--forest-mid) 18%, var(--leaf-light) 34%, var(--forest-mid) 48%, var(--rock) 64%, var(--water) 84%, var(--water-deep) 100%);
  }
  .scene-photo::after {
    content: ""; position: absolute; right: 0; top: 0; width: 220px; height: 260px;
    background: radial-gradient(ellipse at 80% 20%, var(--sky), transparent 70%);
  }
  .info-panel {
    position: absolute; left: 44px; top: 45px; width: 631px; height: 497px;
    background: var(--panel-blue); border-radius: 14px;
    padding: 34px 30px 0 35px; color: var(--text-white);
  }
  .info-heading {
    font-family: "Nunito", sans-serif; font-weight: 800; font-size: 21px; line-height: 26px;
  }
  .info-body {
    font-family: "Didact Gothic", sans-serif; font-size: 18px; line-height: 24.3px; margin-bottom: 21px;
  }
  .portrait-photo {
    position: absolute; left: 328px; top: 472px; width: 380px; height: 428px;
    border-radius: 150px 150px 0 0;
    background: linear-gradient(180deg, var(--hair-gold) 0%, #e2b894 28%, var(--dress-white) 50%, var(--dress-white) 100%);
  }
  .brand {
    position: absolute; left: 50px; top: 600px; width: 320px;
    color: var(--text-white); text-align: center;
  }
  .brand-name {
    font-family: "Didact Gothic", sans-serif; font-size: 60px; line-height: 80px; letter-spacing: 2px;
  }
  .brand-contact {
    font-family: "Open Sans", sans-serif; font-weight: 600; font-size: 20px; line-height: 32px; margin-top: 16px;
  }
</style>
</head>
<body>
  <main class="poster">
    <div class="scene-photo" role="img" aria-label="Photo of a forest waterfall flowing into a turquoise pool"></div>

    <section class="info-panel">
      <h2 class="info-heading">What are benefits of meditation?</h2>
      <p class="info-body">manage stress, reduce anxiety, improve relationships, create inner peace, awaken intuition, aid sleep patterns, lower blood pressure, become less judgemental, connect to spirit</p>

      <h2 class="info-heading">What is meditation?</h2>
      <p class="info-body">A tool to discover the bodies own inner intelligence.<br>Its not about forcing the mind to be quiet, its about finding the stillness thats already there</p>

      <h2 class="info-heading">How will meditation improve my health?</h2>
      <p class="info-body">Doctors are increasingly citing stress as a major contributing factor to most illnesses. Research has shown meditation<br>to be beneficial for wide range of health problems. As stress<br>is greatly reduced through meditation - our minds and<br>our bodies begin to function with<br>maximum effectiveness.</p>
    </section>

    <div class="portrait-photo" role="img" aria-label="Photo of a woman in a white dress meditating cross-legged"></div>

    <div class="brand">
      <div class="brand-name">Calmora</div>
      <div class="brand-contact">www.calmora-studio.com<br>(514) 555-0182</div>
    </div>
  </main>
</body>
</html>
```